PPT template for boutique strategic planning, accounting and taxation firm

We are a boutique firm that provides strategic, accounting and tax advice to our clients. The work we are doing is increasingly strategic work and we are required to produce reports and presentations and our current templates are simply not sufficient.
As you can see from the examples attached, we have very limited skills in house re design! We have attached a PPT document and word document (that should be PPT) that we use regularly as examples of the content. Excel worksheets are regularly embedded into the presentation (in both blue and orange - see below re colours)
Not specific to one area but typically these clients are famous for their own brand and are creating value in their industry through creating their own brand and we want to produce documents of a similar standard.
A Powerpoint Document Slide Template
Cover page layout, back page, intermediate page heading, in colours and styles based on the logo, title styles, and an intermediate or chapter heading slide style. Many of our presentations contain slides with tables, diagrams, flowcharts and text, including simple lists of bullet points. As above, you will see in our style guide that we have three coloured logos – we would like one version in blue and one version in orange please. Again, the cover should be bold and draw attention but remain professional.
We are looking for something that works in both 4:3 and 16:9 (or two templates please)
We like a clear professional and simple look.
Deliverable: PowerPoint template file (.potx extension) for PowerPoint 2007 with at least a “cover” layout, a “title and content” layout, and a simplified slide layout, as well as “back cover”. Please embed any fonts used.
Target Market(s)
Many of our clients are retail clients or have strong brands of their own.
Industry/Entity Type
Accounting
Requirements
Must have
- Harrowby & Co logo on each page.
Must have a cover page (please be bold but professional)
A selection of "standard" slides - dot points, detailed written content, example diagrams, flow charts etc.
A back cover
Nice to have
- We would like to have a copy done in both the blue and orange versions attached. Happy for the winner to complete the other colour after the winner is selected.
Prefer Arial logo but open to suggestions. Must be easy to read and professional
Should not have
- Nothing cartoonish

```html
<!DOCTYPE html>
<html lang="en">
<head>
<meta charset="utf-8">
<title>Harrowby &amp; Co – Presentation Template</title>
<link href="https://fonts.googleapis.com/css2?family=Arimo:wght@400;700&display=swap" rel="stylesheet">
<style>
:root{
  --canvas:#4a4f55;
  --blue:#1a69b3;
  --blue-dark:#14528f;
  --navy:#1c4f86;
  --band:#f2f2f2;
  --fold:#454b51;
  --ink:#4b4f54;
  --text:#5a5a5a;
  --row-light:#f6f6f6;
  --row-blue:#d4e8f8;
  --orange:#f4a12e;
  --teal:#13b4b7;
  --faint:#f3f4f6;
}
*{margin:0;padding:0;box-sizing:border-box}
html,body{width:1032px;height:1200px;overflow:hidden;background:var(--canvas);font-family:"Arimo",Arial,sans-serif}
.slide{position:absolute;width:484px;height:370px;background:#fff;overflow:hidden}
.slide--blue{background:var(--blue)}
.abs{position:absolute}
.watermark{position:absolute;border-radius:50%;border:38px solid var(--faint)}
.wave{position:absolute;left:0;bottom:0;width:484px;height:50px}
.corner-tab{position:absolute;right:0;top:0;width:31px;height:34px;background:var(--blue)}
.brand-small{position:absolute;top:8px;right:40px;display:flex;align-items:center;gap:4px}
.brand-small .dot{width:20px;height:20px;border-radius:50%;background:var(--blue)}
.brand-small .name{font-size:12px;font-weight:700;color:var(--ink);line-height:1;white-space:nowrap}
.brand-small .tag{font-size:3.4px;color:var(--ink);font-weight:700;margin-top:2px;white-space:nowrap}
.band{position:absolute;left:0;width:484px;background:var(--band)}
.card{position:absolute;background:#fff;display:flex;flex-direction:column;align-items:center;justify-content:center}
.brand-large{display:flex;align-items:center;gap:10px}
.brand-large .dot{width:52px;height:52px;border-radius:50%;background:var(--blue)}
.brand-large .name{font-size:29px;font-weight:700;color:var(--ink);line-height:1}
.brand-large .tag{font-size:7px;color:var(--blue);font-weight:700;margin-top:4px}
.fold{position:absolute;width:42px;height:34px}
.title{position:absolute;left:40px;font-size:15px;font-weight:700;color:var(--ink);letter-spacing:-.2px}
.subtitle{position:absolute;left:40px;font-size:12px;color:var(--blue)}
.body{position:absolute;left:40px;width:406px;font-size:10.4px;line-height:13.6px;color:var(--text)}
.body p+p{margin-top:13px}
.rule{position:absolute;left:40px;width:406px;height:1px;background:var(--blue)}
.lead{position:absolute;left:40px;width:406px;font-size:10px;line-height:13.6px;color:var(--blue)}
.table{position:absolute;left:40px;top:50px;width:412px}
.table__head{height:38px;background:var(--blue);color:#fff;font-size:12px;padding:13px 19px}
.table__row{height:21.3px;display:flex;align-items:center;font-size:10px;color:var(--text)}
.table__row:nth-child(odd){background:var(--row-light)}
.table__row:nth-child(even){background:var(--row-blue)}
.table__row span{flex:1;padding-left:21px}
.table__row .mark{width:48px;height:100%;border-left:1px solid #fff;display:flex;align-items:center;justify-content:center}
.member{position:absolute;top:75px;width:131px}
.member__photo{height:68px;background:var(--blue)}
.member__name{margin-top:21px;text-align:center;font-size:12px;font-weight:700;color:var(--navy)}
.member__role{text-align:center;font-size:10px;color:var(--blue);margin-top:1px}
.member__rule{height:2px;background:var(--blue);margin-top:9px}
.member__bio{margin-top:14px;font-size:10px;line-height:13.6px;color:var(--text)}
.callout{position:absolute;left:313px;width:152px;height:75px;padding:13px 16px 0 26px;color:#fff;font-size:8.4px;line-height:11.5px}
.callout::before{content:"";position:absolute;left:-9px;top:28px;width:18px;height:18px;border-radius:50%;background:#fff}
.callout--orange{background:var(--orange)}
.callout--teal{background:var(--teal)}
.callout--blue{background:var(--blue)}
.social{display:flex;gap:6px;margin-top:16px}
.social i{display:block;width:27px;height:27px;border-radius:50%;background:var(--blue)}
</style>
</head>
<body>

<section class="slide slide--blue" style="left:26px;top:32px">
  <div class="band" style="top:150px;height:128px"></div>
  <svg class="fold" style="left:79px;top:244px" viewBox="0 0 42 34"><path d="M0 0H42V34Z" fill="#454b51"/></svg>
  <svg class="fold" style="left:363px;top:244px" viewBox="0 0 42 34"><path d="M0 0H42L0 34Z" fill="#454b51"/></svg>
  <div class="card" style="left:79px;top:115px;width:326px;height:129px">
    <div class="brand-large"><div class="dot"></div><div><div class="name">Harrowby &amp; Co</div><div class="tag">Accounting, Taxation &amp; Strategic Business Advisors</div></div></div>
  </div>
</section>

<section class="slide" style="left:524px;top:32px">
  <div class="watermark" style="left:150px;top:30px;width:240px;height:240px"></div>
  <div class="corner-tab"></div>
  <div class="brand-small"><div class="dot"></div><div><div class="name">Harrowby &amp; Co</div><div class="tag">Accounting, Taxation &amp; Strategic Business Advisors</div></div></div>
  <h1 class="title" style="top:34px">Lorem ipsum.</h1>
  <div class="subtitle" style="top:52px">Subtitle</div>
  <div class="body" style="top:75px">
    <p>Lorem ipsum dolor sit amet, consectetur adipiscing elit. Nullam a orci sit amet magna varius porttitor eu quis nisi. Ut viverra mi a leo lacinia molestie non sed quam. Pellentesque habitant morbi tristique senectus et netus et malesuada fames ac turpis egestas. Suspendisse tempor erat lorem, ac blandit libero porttitor vitae. Suspendisse faucibus nisl sed libero tristique, non luctus nulla viverra. Aenean porta quam sed accumsan imperdiet. Maecenas convallis auctor consectetur. Praesent posuere ullamcorper lectus sit amet viverra.</p>
    <p>Donec egestas nec leo in fringilla. Morbi sem metus, consequat non malesuada in, dictum nec elit. Phasellus quam eros, euismod ac enim vel, auctor dignissim ligula. Integer tempor tellus purus, ac cursus nisi sagittis pellentesque. Nullam luctus fermentum rhoncus.</p>
  </div>
  <div class="rule" style="top:248px"></div>
  <div class="lead" style="top:253px">Quisque commodo felis vitae aliquam bibendum. Curabitur sapien velit, egestas eget eros vitae, fermentum pellentesque sapien.</div>
  <div class="rule" style="top:290px"></div>
  <svg class="wave" viewBox="0 0 484 50"><path d="M0 20Q260 14 484 2" fill="none" stroke="#1a69b3" stroke-width="2"/><path d="M0 30Q260 22 484 8V50H0Z" fill="#1a69b3"/></svg>
</section>

<section class="slide" style="left:26px;top:414px">
  <div class="watermark" style="left:160px;top:40px;width:240px;height:240px"></div>
  <div class="corner-tab"></div>
  <div class="brand-small"><div class="dot"></div><div><div class="name">Harrowby &amp; Co</div><div class="tag">Accounting, Taxation &amp; Strategic Business Advisors</div></div></div>
  <div class="table">
    <div class="table__head">Explanation or title here</div>
    <div class="table__rows">
      <div class="table__row"><span>Lorem ipsum dolor sit amet, consectetur adipiscing elit.</span><div class="mark"><svg width="12" height="10"><path d="M1 5L4.5 8.5L11 1" fill="none" stroke="#3a9a3a" stroke-width="1.6"/></svg></div></div>
      <div class="table__row"><span>Lorem ipsum dolor sit amet, consectetur adipiscing elit.</span><div class="mark"><svg width="12" height="12"><circle cx="6" cy="6" r="6" fill="#e23b3b"/><path d="M3.8 3.8L8.2 8.2M8.2 3.8L3.8 8.2" stroke="#fff" stroke-width="1.4"/></svg></div></div>
      <div class="table__row"><span>Lorem ipsum dolor sit amet, consectetur adipiscing elit.</span><div class="mark"><svg width="12" height="10"><path d="M1 5L4.5 8.5L11 1" fill="none" stroke="#3a9a3a" stroke-width="1.6"/></svg></div></div>
      <div class="table__row"><span>Lorem ipsum dolor sit amet, consectetur adipiscing elit.</span><div class="mark"><svg width="12" height="10"><path d="M1 5L4.5 8.5L11 1" fill="none" stroke="#3a9a3a" stroke-width="1.6"/></svg></div></div>
      <div class="table__row"><span>Lorem ipsum dolor sit amet, consectetur adipiscing elit.</span><div class="mark"><svg width="12" height="10"><path d="M1 5L4.5 8.5L11 1" fill="none" stroke="#3a9a3a" stroke-width="1.6"/></svg></div></div>
      <div class="table__row"><span>Lorem ipsum dolor sit amet, consectetur adipiscing elit.</span><div class="mark"><svg width="12" height="12"><circle cx="6" cy="6" r="6" fill="#e23b3b"/><path d="M3.8 3.8L8.2 8.2M8.2 3.8L3.8 8.2" stroke="#fff" stroke-width="1.4"/></svg></div></div>
      <div class="table__row"><span>Lorem ipsum dolor sit amet, consectetur adipiscing elit.</span><div class="mark"><svg width="12" height="12"><circle cx="6" cy="6" r="6" fill="#e23b3b"/><path d="M3.8 3.8L8.2 8.2M8.2 3.8L3.8 8.2" stroke="#fff" stroke-width="1.4"/></svg></div></div>
      <div class="table__row"><span>Lorem ipsum dolor sit amet, consectetur adipiscing elit.</span><div class="mark"><svg width="12" height="10"><path d="M1 5L4.5 8.5L11 1" fill="none" stroke="#3a9a3a" stroke-width="1.6"/></svg></div></div>
      <div class="table__row"><span>Lorem ipsum dolor sit amet, consectetur adipiscing elit.</span><div class="mark"><svg width="12" height="10"><path d="M1 5L4.5 8.5L11 1" fill="none" stroke="#3a9a3a" stroke-width="1.6"/></svg></div></div>
      <div class="table__row"><span>Lorem ipsum dolor sit amet, consectetur adipiscing elit.</span><div class="mark"><svg width="12" height="12"><circle cx="6" cy="6" r="6" fill="#e23b3b"/><path d="M3.8 3.8L8.2 8.2M8.2 3.8L3.8 8.2" stroke="#fff" stroke-width="1.4"/></svg></div></div>
    </div>
  </div>
  <svg class="wave" viewBox="0 0 484 50"><path d="M0 20Q260 14 484 2" fill="none" stroke="#1a69b3" stroke-width="2"/><path d="M0 30Q260 22 484 8V50H0Z" fill="#1a69b3"/></svg>
</section>

<section class="slide" style="left:524px;top:414px">
  <div class="watermark" style="left:150px;top:50px;width:240px;height:240px"></div>
  <div class="corner-tab"></div>
  <div class="brand-small"><div class="dot"></div><div><div class="name">Harrowby &amp; Co</div><div class="tag">Accounting, Taxation &amp; Strategic Business Advisors</div></div></div>
  <div class="member" style="left:32px"><div class="member__photo" role="img" aria-label="Team member photo placeholder"></div><div class="member__name">JOHN SMITH</div><div class="member__role">Executive director</div><div class="member__rule"></div><div class="member__bio">Lorem ipsum dolor sit amet, consectetur adipiscing elit. Mauris eu nulla massa. Nulla quis tellus ultrices, gravida justo ut, rhoncus</div></div>
  <div class="member" style="left:174px"><div class="member__photo" role="img" aria-label="Team member photo placeholder"></div><div class="member__name">JOHN SMITH</div><div class="member__role">Executive director</div><div class="member__rule"></div><div class="member__bio">Lorem ipsum dolor sit amet, consectetur adipiscing elit. Mauris eu nulla massa. Nulla quis tellus ultrices, gravida justo ut, rhoncus</div></div>
  <div class="member" style="left:315px"><div class="member__photo" role="img" aria-label="Team member photo placeholder"></div><div class="member__name">JOHN SMITH</div><div class="member__role">Executive director</div><div class="member__rule"></div><div class="member__bio">Lorem ipsum dolor sit amet, consectetur adipiscing elit. Mauris eu nulla massa. Nulla quis tellus ultrices, gravida justo ut, rhoncus</div></div>
  <svg class="wave" viewBox="0 0 484 50"><path d="M0 20Q260 14 484 2" fill="none" stroke="#1a69b3" stroke-width="2"/><path d="M0 30Q260 22 484 8V50H0Z" fill="#1a69b3"/></svg>
</section>

<section class="slide" style="left:26px;top:800px;height:372px">
  <div class="watermark" style="left:150px;top:50px;width:250px;height:250px"></div>
  <div class="corner-tab"></div>
  <div class="brand-small"><div class="dot"></div><div><div class="name">Harrowby &amp; Co</div><div class="tag">Accounting, Taxation &amp; Strategic Business Advisors</div></div></div>
  <h2 class="title" style="top:32px">Lorem ipsum.</h2>
  <div class="subtitle" style="top:50px">Subtitle</div>
  <svg class="abs" style="left:6px;top:25px" width="300" height="240" viewBox="0 0 300 240">
    <path d="M15 140A135 65 0 0 0 285 140L285 165A135 65 0 0 1 15 165Z" fill="#14528f"/>
    <path d="M150 140L15 140A135 65 0 1 0 150 75Z" fill="#1a7cc9"/>
    <path d="M150 140L108.3 78.2A135 65 0 0 0 15 140Z" fill="#13b4b7"/>
    <path d="M150 140L150 75A135 65 0 0 0 108.3 78.2Z" fill="#f4a12e"/>
    <g font-family="Arimo, Arial, sans-serif" font-weight="700" font-size="27" fill="#e9edf1" stroke="#6b7480" stroke-width=".8">
      <text x="186" y="149">75%</text><text x="44" y="149">20%</text><text x="122" y="108">5%</text>
    </g>
  </svg>
  <div class="callout callout--orange" style="top:64px">Lorem ipsum dolor sit amet, consectetur adipiscing elit. Nullam a orci sit amet magna varius porttitor eu quis nisi.</div>
  <div class="callout callout--teal" style="top:140px">Lorem ipsum dolor sit amet, consectetur adipiscing elit. Nullam a orci sit amet magna varius porttitor eu quis nisi.</div>
  <div class="callout callout--blue" style="top:216px">Lorem ipsum dolor sit amet, consectetur adipiscing elit. Nullam a orci sit amet magna varius porttitor eu quis nisi.</div>
  <svg class="wave" viewBox="0 0 484 50"><path d="M0 20Q260 14 484 2" fill="none" stroke="#1a69b3" stroke-width="2"/><path d="M0 30Q260 22 484 8V50H0Z" fill="#1a69b3"/></svg>
</section>

<section class="slide slide--blue" style="left:524px;top:800px;height:372px">
  <div class="band" style="top:100px;height:132px"></div>
  <svg class="fold" style="left:78px;top:199px" viewBox="0 0 42 34"><path d="M0 0H42V34Z" fill="#454b51"/></svg>
  <svg class="fold" style="left:364px;top:199px" viewBox="0 0 42 34"><path d="M0 0H42L0 34Z" fill="#454b51"/></svg>
  <div class="card" style="left:78px;top:70px;width:328px;height:129px">
    <div class="brand-large" style="transform:scale(.75)"><div class="dot"></div><div><div class="name">Harrowby &amp; Co</div><div class="tag">Accounting, Taxation &amp; Strategic Business Advisors</div></div></div>
    <div class="social"><i></i><i></i><i></i><i></i><i></i></div>
  </div>
</section>

</body>
</html>
```